Business Card Design

Lawyer
Business name "HarlowLaw"
Areas of expertise:
property
commercial
trusts
immigration
franchising
I want the following quote on the back of the card somewhere.
"Education is when you read the fine print,
experience is what you get if you don't." Miles Corbell
Probably the "areas of expertise" should be on the back also to avoid cluttering the front.
As for colours, I like the shades of blue used on qerivo.com.
The basic part of the card with the contact info needs to be white and uncluttered.
Target Market(s)
small to medium sized self employed business people
Industry/Entity Type
Business
Contact Information for Business Card
Dennis Harlow
Phone + 64 9 517 4460
Fax: + 64 9 517 4461
PO Box 742
Tawhera Bay
Rangimoa 3417
NZ
email: dennis@pinecrestlegal.co.nz

```html
<!DOCTYPE html>
<html lang="en">
<head>
<meta charset="utf-8">
<title>HarlowLaw Business Card</title>
<link rel="stylesheet" href="https://fonts.googleapis.com/css2?family=Arimo:wght@400;700&display=swap">
<style>
  :root {
    --brand-blue: #0a8ccf;
    --ink-grey: #555a5e;
    --rule-grey: #8a8f93;
    --card-border: #b9bcbf;
    --paper: #ffffff;
  }
  * { margin: 0; padding: 0; box-sizing: border-box; }
  html, body { width: 1200px; height: 1000px; overflow: hidden; background: var(--paper); }
  body { position: relative; font-family: "Arimo", Arial, sans-serif; }

  .card { position: absolute; top: 365px; width: 468px; height: 271px; overflow: hidden; }
  .card-front { left: 113px; background: var(--paper); border: 1px solid var(--card-border); }
  .card-back { left: 620px; background: var(--brand-blue); color: #fff; }

  .front-brand { position: absolute; left: 28px; top: 180px; display: flex; align-items: center; gap: 7px; }
  .brand-dot { width: 13px; height: 13px; border-radius: 50%; background: var(--brand-blue); }
  .front-brand .brand-name { font-size: 30px; line-height: 34px; font-weight: 700; color: var(--brand-blue); letter-spacing: -0.5px; }

  .contact { position: absolute; left: 296px; top: 102px; color: var(--ink-grey); font-size: 10.5px; }
  .contact-name { font-size: 15px; font-weight: 700; color: var(--brand-blue); margin-bottom: 8px; }
  .contact-row { display: flex; align-items: flex-start; gap: 6px; line-height: 15px; margin-bottom: 2px; letter-spacing: 0.1px; }
  .contact-row svg { flex: none; margin-top: 2px; }
  .rule { width: 44px; height: 1px; background: var(--rule-grey); margin: 9px 0 11px; }

  .back-brand { position: absolute; left: 0; right: 0; top: 56px; display: flex; flex-direction: column; align-items: center; gap: 8px; }
  .back-brand .brand-dot { background: #fff; width: 16px; height: 16px; }
  .back-brand .brand-name { font-size: 26px; font-weight: 700; color: #fff; letter-spacing: -0.3px; }

  .expertise { position: absolute; left: 0; right: 0; top: 140px; text-align: center; }
  .expertise-label { font-size: 10px; letter-spacing: 0.3px; }
  .expertise-list { font-size: 11.5px; font-weight: 700; margin-top: 6px; letter-spacing: 0.2px; }

  .quote { position: absolute; left: 122px; top: 194px; font-size: 11px; line-height: 14px; letter-spacing: 0.3px; }
  .quote-author { display: block; text-align: right; font-size: 10px; margin-top: 2px; }
</style>
</head>
<body>
  <section class="card card-front">
    <div class="front-brand">
      <span class="brand-dot"></span>
      <span class="brand-name">HarlowLaw</span>
    </div>
    <div class="contact">
      <div class="contact-name">Dennis Harlow</div>
      <div class="contact-row">
        <svg width="11" height="10" viewBox="0 0 11 10"><path d="M1 3 Q5.5 0 10 3 L9 5 L7.5 4 L7.5 3 Q5.5 2 3.5 3 L3.5 4 L2 5 Z M2.5 5.5 L8.5 5.5 L9.5 9.5 L1.5 9.5 Z" fill="var(--brand-blue)"/></svg>
        <span>+ 64 9 517 4460</span>
      </div>
      <div class="contact-row">
        <svg width="11" height="10" viewBox="0 0 11 10"><rect x="0.5" y="3" width="10" height="6.5" fill="var(--brand-blue)"/><rect x="3" y="0.5" width="5" height="3" fill="none" stroke="var(--brand-blue)"/><rect x="2" y="5" width="4" height="1.2" fill="#fff"/></svg>
        <span>+ 64 9 517 4461</span>
      </div>
      <div class="rule"></div>
      <div class="contact-row">
        <svg width="11" height="10" viewBox="0 0 11 10"><path d="M0.5 3 L5.5 0.5 L10.5 3 Z" fill="var(--brand-blue)"/><rect x="1.5" y="3.5" width="1.3" height="4.5" fill="var(--brand-blue)"/><rect x="4.8" y="3.5" width="1.3" height="4.5" fill="var(--brand-blue)"/><rect x="8.1" y="3.5" width="1.3" height="4.5" fill="var(--brand-blue)"/><rect x="0.5" y="8.5" width="10" height="1.5" fill="var(--brand-blue)"/></svg>
        <span>PO Box 742 Tawhera Bay<br>Rangimoa 3417 NZ</span>
      </div>
      <div class="rule"></div>
      <div class="contact-row">
        <svg width="11" height="10" viewBox="0 0 11 10"><rect x="0.5" y="1.5" width="10" height="7.5" fill="var(--brand-blue)"/><path d="M0.5 1.5 L5.5 5.5 L10.5 1.5" fill="none" stroke="#fff" stroke-width="0.9"/></svg>
        <span>dennis@pinecrestlegal.co.nz</span>
      </div>
    </div>
  </section>

  <section class="card card-back">
    <div class="back-brand">
      <span class="brand-dot"></span>
      <span class="brand-name">HarlowLaw</span>
    </div>
    <div class="expertise">
      <div class="expertise-label">Areas Of Expertise:</div>
      <div class="expertise-list">Property, Commercial, Trusts, Immigration, Franchising</div>
    </div>
    <blockquote class="quote">
      “Education is when you read the fine print,<br>
      experience is what you get if you don’t.”
      <span class="quote-author">- Miles Corbell</span>
    </blockquote>
  </section>
</body>
</html>
```